Harborline Toma's Chinese/Dim Sum Restaurant Menu

Harborline Toma's is a seafood-asian fusion restaurant featuring dim sum and other classical asian fusion items.

We need a menu design that includes both our food menu and our drink menu.

Food menu: Needs to have space for descriptions of food (please just include a place holder and we will input them later). See attached for food menu items.

Drink menu: Just lists of items with prices. See attached Jade Lantern Menu- please include the same items, but rebrand for Harborline Toma's.

The menus must be able to be printed in a 4.25x11in paper.

We want something modern and contemporary. My boss likes geometrical design aspects and minimalism. So, nothing too ornate. But, it has to be different from the Jade Lantern menus. Colors can be black, red, gold or blue- but it must be able to be tied into our black and red Harborline Toma's logo. Including elements of Chinese culture, especially fishing, is a plus, but not necessary.

We also need this in ai format when we download final copy so we can edit in the future.

UPDATE: Please note, we already have a logo.

Target Market(s)

Upscale family diners

Industry/Entity Type

Chinese Food

Font styles to use
Serif
Sans Serif

Colors
0054AA
0677BA
7BADD7
CADEEF
E8F1F8
0094D4
00A9DD
6FCCEA
C7EBF8
E9F6FB
FFC000
F8CF3A
FAE287
FDF2CF
FEFAEE
EB3D1F
EC4F4E
F09395
F8D3D4
FCEDEE

Requirements
Must have
• Classic, minimalist, elegant

```html
<!DOCTYPE html>
<html lang="en">
<head>
<meta charset="utf-8">
<title>Harborline Toma's – Food Menu</title>
<link href="https://fonts.googleapis.com/css2?family=Montserrat:wght@400;600;800&family=Oswald:wght@500;600&family=Roboto:wght@400;500&display=swap" rel="stylesheet">
<style>
  :root{
    --red:#e0312b;
    --red-soft:#fcedee;
    --ink:#1c1c1c;
    --grey:#8a8a8a;
    --paper:#ffffff;
    --backdrop:#ececec;
  }
  *{box-sizing:border-box;margin:0;padding:0}
  html,body{width:849px;height:1200px;overflow:hidden}
  body{background:var(--backdrop);position:relative;font-family:"Roboto",sans-serif;color:var(--ink)}

  .page{position:absolute;width:312px;height:520px;background:var(--paper);box-shadow:0 2px 6px rgba(0,0,0,.18);overflow:hidden}
  .page--cover{left:108px;top:52px}
  .page--dimsum{left:430px;top:52px}
  .page--appetizers{left:108px;top:588px}
  .page--rice{left:430px;top:588px}

  .edge-line{position:absolute;top:14px;bottom:14px;width:1.5px;background:var(--red)}
  .edge-line--left{left:9px}
  .edge-line--right{right:9px}
  .edge-line--thin{width:1px;opacity:.7}

  /* name set as plain text, single line, one colour and weight */
  .brand-name{font-family:"Montserrat",sans-serif;font-weight:600;color:var(--ink);white-space:nowrap;line-height:1}

  /* cover */
  .cover-brand{position:absolute;left:0;right:0;top:200px;text-align:center}
  .cover-brand .brand-name{font-size:22px;letter-spacing:.3px}
  .cover-title{margin-top:30px;font-family:"Oswald",sans-serif;font-weight:600;font-size:15px;letter-spacing:4px;color:var(--red)}

  /* interior */
  .page-header{position:absolute;left:24px;right:16px;top:14px;height:8px;border-bottom:.6px solid #cfcfcf}
  .columns{position:absolute;left:24px;right:16px;top:34px;bottom:16px;display:grid;grid-template-columns:1fr 1fr;column-gap:18px}
  .section + .section{margin-top:18px}
  .section-head{position:relative;height:44px;margin-bottom:8px}
  .section-title{position:absolute;left:0;bottom:0;font-family:"Oswald",sans-serif;font-weight:600;font-size:10.5px;letter-spacing:1.2px;line-height:1;color:var(--red);display:flex;align-items:center;gap:4px;white-space:nowrap}
  .section-title::before{content:"";display:block;width:8px;height:1px;background:var(--red)}
  .section-icon{position:absolute;right:0;top:0;width:32px;height:30px;background:var(--red-soft);border-radius:4px}

  .dish-list{list-style:none}
  .dish{margin-bottom:12.5px}
  .dish-line{display:flex;justify-content:space-between;align-items:baseline}
  .dish-name{font-family:"Montserrat",sans-serif;font-weight:600;font-size:5.6px;letter-spacing:.4px;text-transform:uppercase;color:var(--red)}
  .dish-price{font-family:"Montserrat",sans-serif;font-weight:600;font-size:6px;color:var(--ink)}
  .dish-desc{font-size:4.4px;line-height:1.45;color:var(--grey);margin-top:2px;max-width:90%}

  .page--appetizers .dish{margin-bottom:13.5px}
  .page--appetizers .section-head--plain{height:30px}
  .page--appetizers .seafood-list .dish{margin-bottom:11.5px}

  .end-brand{position:absolute;right:30px;bottom:56px;text-align:right}
  .end-brand .brand-name{font-size:13px;letter-spacing:.2px}
</style>
</head>
<body>

<section class="page page--cover">
  <div class="edge-line edge-line--left"></div>
  <div class="cover-brand">
    <div class="brand-name">Harborline Toma's</div>
    <div class="cover-title">FOOD MENU</div>
  </div>
</section>

<section class="page page--dimsum">
  <div class="edge-line edge-line--left edge-line--thin"></div>
  <div class="page-header"></div>
  <div class="columns">
    <div class="section">
      <div class="section-head"><h2 class="section-title">DIM SUM</h2><div class="section-icon" role="img" aria-label="Line drawing of a dim sum steamer basket"></div></div>
      <ul class="dish-list">
        <li class="dish"><div class="dish-line"><span class="dish-name">Shrimp Har Gow</span><span class="dish-price">9</span></div><p class="dish-desc">Dish description to be added here later.</p></li>
        <li class="dish"><div class="dish-line"><span class="dish-name">Pork Siu Mai</span><span class="dish-price">8</span></div><p class="dish-desc">Dish description to be added here later.</p></li>
        <li class="dish"><div class="dish-line"><span class="dish-name">Crystal Dumplings</span><span class="dish-price">9</span></div><p class="dish-desc">Dish description to be added here later.</p></li>
        <li class="dish"><div class="dish-line"><span class="dish-name">Char Siu Bao</span><span class="dish-price">7</span></div><p class="dish-desc">Dish description to be added here later.</p></li>
        <li class="dish"><div class="dish-line"><span class="dish-name">Turnip Cake</span><span class="dish-price">6</span></div><p class="dish-desc">Dish description to be added here later.</p></li>
        <li class="dish"><div class="dish-line"><span class="dish-name">Chicken Feet</span><span class="dish-price">7</span></div><p class="dish-desc">Dish description to be added here later.</p></li>
        <li class="dish"><div class="dish-line"><span class="dish-name">Rice Noodle Roll</span><span class="dish-price">8</span></div><p class="dish-desc">Dish description to be added here later.</p></li>
        <li class="dish"><div class="dish-line"><span class="dish-name">Taro Puffs</span><span class="dish-price">7</span></div><p class="dish-desc">Dish description to be added here later.</p></li>
        <li class="dish"><div class="dish-line"><span class="dish-name">Sticky Rice Wrap</span><span class="dish-price">8</span></div><p class="dish-desc">Dish description to be added here later.</p></li>
        <li class="dish"><div class="dish-line"><span class="dish-name">Egg Custard Tart</span><span class="dish-price">6</span></div><p class="dish-desc">Dish description to be added here later.</p></li>
      </ul>
    </div>
    <div>
      <div class="section">
        <div class="section-head"><h2 class="section-title">SOUPS</h2><div class="section-icon" role="img" aria-label="Line drawing of a soup bowl with chopsticks"></div></div>
        <ul class="dish-list">
          <li class="dish"><div class="dish-line"><span class="dish-name">Hot and Sour</span><span class="dish-price">6</span></div><p class="dish-desc">Dish description to be added here later.</p></li>
          <li class="dish"><div class="dish-line"><span class="dish-name">Wonton Soup</span><span class="dish-price">6</span></div><p class="dish-desc">Dish description to be added here later.</p></li>
          <li class="dish"><div class="dish-line"><span class="dish-name">Seafood Tofu Soup</span><span class="dish-price">8</span></div><p class="dish-desc">Dish description to be added here later.</p></li>
        </ul>
      </div>
      <div class="section">
        <div class="section-head"><h2 class="section-title">VEGGIE</h2><div class="section-icon" role="img" aria-label="Line drawing of broccoli"></div></div>
        <ul class="dish-list">
          <li class="dish"><div class="dish-line"><span class="dish-name">Garlic Greens</span><span class="dish-price">9</span></div><p class="dish-desc">Dish description to be added here later.</p></li>
          <li class="dish"><div class="dish-line"><span class="dish-name">Mapo Tofu</span><span class="dish-price">10</span></div><p class="dish-desc">Dish description to be added here later.</p></li>
          <li class="dish"><div class="dish-line"><span class="dish-name">Buddha Delight</span><span class="dish-price">11</span></div><p class="dish-desc">Dish description to be added here later.</p></li>
        </ul>
      </div>
    </div>
  </div>
</section>

<section class="page page--appetizers">
  <div class="edge-line edge-line--left"></div>
  <div class="columns" style="top:18px">
    <div class="section">
      <div class="section-head section-head--plain"><h2 class="section-title">APPETIZERS</h2></div>
      <ul class="dish-list">
        <li class="dish"><div class="dish-line"><span class="dish-name">Spring Rolls</span><span class="dish-price">6</span></div><p class="dish-desc">Dish description to be added here later.</p></li>
        <li class="dish"><div class="dish-line"><span class="dish-name">Crab Rangoon</span><span class="dish-price">8</span></div><p class="dish-desc">Dish description to be added here later.</p></li>
        <li class="dish"><div class="dish-line"><span class="dish-name">Salt Pepper Squid</span><span class="dish-price">10</span></div><p class="dish-desc">Dish description to be added here later.</p></li>
        <li class="dish"><div class="dish-line"><span class="dish-name">Shrimp Toast</span><span class="dish-price">8</span></div><p class="dish-desc">Dish description to be added here later.</p></li>
        <li class="dish"><div class="dish-line"><span class="dish-name">Potstickers</span><span class="dish-price">7</span></div><p class="dish-desc">Dish description to be added here later.</p></li>
        <li class="dish"><div class="dish-line"><span class="dish-name">Scallion Pancake</span><span class="dish-price">6</span></div><p class="dish-desc">Dish description to be added here later.</p></li>
        <li class="dish"><div class="dish-line"><span class="dish-name">Fried Calamari</span><span class="dish-price">9</span></div><p class="dish-desc">Dish description to be added here later.</p></li>
        <li class="dish"><div class="dish-line"><span class="dish-name">Sesame Wings</span><span class="dish-price">9</span></div><p class="dish-desc">Dish description to be added here later.</p></li>
        <li class="dish"><div class="dish-line"><span class="dish-name">Lettuce Wraps</span><span class="dish-price">10</span></div><p class="dish-desc">Dish description to be added here later.</p></li>
        <li class="dish"><div class="dish-line"><span class="dish-name">Edamame</span><span class="dish-price">5</span></div><p class="dish-desc">Dish description to be added here later.</p></li>
        <li class="dish"><div class="dish-line"><span class="dish-name">Cucumber Salad</span><span class="dish-price">5</span></div><p class="dish-desc">Dish description to be added here later.</p></li>
        <li class="dish"><div class="dish-line"><span class="dish-name">Pork Dumplings</span><span class="dish-price">8</span></div><p class="dish-desc">Dish description to be added here later.</p></li>
      </ul>
    </div>
    <div class="section">
      <div class="section-head" style="height:46px"><h2 class="section-title">SEAFOOD</h2><div class="section-icon" role="img" aria-label="Line drawing of two fish"></div></div>
      <ul class="dish-list seafood-list">
        <li class="dish"><div class="dish-line"><span class="dish-name">Lobster Ginger</span><span class="dish-price">28</span></div><p class="dish-desc">Dish description to be added here later.</p></li>
        <li class="dish"><div class="dish-line"><span class="dish-name">Black Bean Clams</span><span class="dish-price">16</span></div><p class="dish-desc">Dish description to be added here later.</p></li>
        <li class="dish"><div class="dish-line"><span class="dish-name">Steamed Sea Bass</span><span class="dish-price">24</span></div><p class="dish-desc">Dish description to be added here later.</p></li>
        <li class="dish"><div class="dish-line"><span class="dish-name">Kung Pao Shrimp</span><span class="dish-price">17</span></div><p class="dish-desc">Dish description to be added here later.</p></li>
        <li class="dish"><div class="dish-line"><span class="dish-name">Honey Walnut Prawns</span><span class="dish-price">19</span></div><p class="dish-desc">Dish description to be added here later.</p></li>
        <li class="dish"><div class="dish-line"><span class="dish-name">Salt Pepper Crab</span><span class="dish-price">26</span></div><p class="dish-desc">Dish description to be added here later.</p></li>
        <li class="dish"><div class="dish-line"><span class="dish-name">Scallops XO</span><span class="dish-price">22</span></div><p class="dish-desc">Dish description to be added here later.</p></li>
        <li class="dish"><div class="dish-line"><span class="dish-name">Sweet Sour Fish</span><span class="dish-price">18</span></div><p class="dish-desc">Dish description to be added here later.</p></li>
        <li class="dish"><div class="dish-line"><span class="dish-name">Garlic Mussels</span><span class="dish-price">16</span></div><p class="dish-desc">Dish description to be added here later.</p></li>
        <li class="dish"><div class="dish-line"><span class="dish-name">Chili Prawns</span><span class="dish-price">19</span></div><p class="dish-desc">Dish description to be added here later.</p></li>
        <li class="dish"><div class="dish-line"><span class="dish-name">Curry Squid</span><span class="dish-price">15</span></div><p class="dish-desc">Dish description to be added here later.</p></li>
        <li class="dish"><div class="dish-line"><span class="dish-name">Ginger Oysters</span><span class="dish-price">21</span></div><p class="dish-desc">Dish description to be added here later.</p></li>
      </ul>
    </div>
  </div>
</section>

<section class="page page--rice">
  <div class="edge-line edge-line--right"></div>
  <div class="columns" style="left:16px;right:24px;top:18px">
    <div class="section">
      <div class="section-head"><h2 class="section-title">RICE &amp; NOODLES</h2><div class="section-icon" role="img" aria-label="Line drawing of a noodle bowl"></div></div>
      <ul class="dish-list">
        <li class="dish"><div class="dish-line"><span class="dish-name">Yangzhou Fried Rice</span><span class="dish-price">12</span></div><p class="dish-desc">Dish description to be added here later.</p></li>
        <li class="dish"><div class="dish-line"><span class="dish-name">Beef Chow Fun</span><span class="dish-price">14</span></div><p class="dish-desc">Dish description to be added here later.</p></li>
        <li class="dish"><div class="dish-line"><span class="dish-name">Seafood Lo Mein</span><span class="dish-price">16</span></div><p class="dish-desc">Dish description to be added here later.</p></li>
        <li class="dish"><div class="dish-line"><span class="dish-name">Singapore Noodles</span><span class="dish-price">13</span></div><p class="dish-desc">Dish description to be added here later.</p></li>
        <li class="dish"><div class="dish-line"><span class="dish-name">Crab Fried Rice</span><span class="dish-price">17</span></div><p class="dish-desc">Dish description to be added here later.</p></li>
        <li class="dish"><div class="dish-line"><span class="dish-name">Dan Dan Noodles</span><span class="dish-price">12</span></div><p class="dish-desc">Dish description to be added here later.</p></li>
        <li class="dish"><div class="dish-line"><span class="dish-name">Pineapple Rice</span><span class="dish-price">13</span></div><p class="dish-desc">Dish description to be added here later.</p></li>
        <li class="dish"><div class="dish-line"><span class="dish-name">Shrimp Pad Thai</span><span class="dish-price">15</span></div><p class="dish-desc">Dish description to be added here later.</p></li>
        <li class="dish"><div class="dish-line"><span class="dish-name">Duck Noodle Soup</span><span class="dish-price">15</span></div><p class="dish-desc">Dish description to be added here later.</p></li>
        <li class="dish"><div class="dish-line"><span class="dish-name">Egg Fried Rice</span><span class="dish-price">10</span></div><p class="dish-desc">Dish description to be added here later.</p></li>
      </ul>
    </div>
    <div class="section">
      <div class="section-head"><h2 class="section-title">SWEET &amp; DESSERTS</h2><div class="section-icon" role="img" aria-label="Line drawing of a slice of cake"></div></div>
      <ul class="dish-list">
        <li class="dish"><div class="dish-line"><span class="dish-name">Mango Pudding</span><span class="dish-price">6</span></div><p class="dish-desc">Dish description to be added here later.</p></li>
        <li class="dish"><div class="dish-line"><span class="dish-name">Sesame Balls</span><span class="dish-price">6</span></div><p class="dish-desc">Dish description to be added here later.</p></li>
        <li class="dish"><div class="dish-line"><span class="dish-name">Red Bean Soup</span><span class="dish-price">5</span></div><p class="dish-desc">Dish description to be added here later.</p></li>
      </ul>
    </div>
  </div>
  <div class="end-brand">
    <div class="brand-name">Harborline Toma's</div>
  </div>
</section>

</body>
</html>
```